Business Card Design

My business is writing crime novels to entertain readers. I write legal thrillers and mysteries. I need a card for publishers, agents, other authors, and media.

Industry/Entity Type

Legal

Contact Information for Business Card

Paul Ostrander
www.ostranderthrillers.example
paulbostrander@mailbox.example
0064 27 5139427

```html
<!DOCTYPE html>
<html lang="en">
<head>
<meta charset="utf-8">
<title>Paul Ostrander – Business Card</title>
<link href="https://fonts.googleapis.com/css2?family=Urbanist:wght@400;500;700&display=swap" rel="stylesheet">
<style>
  :root {
    --card-grey: #6f6f6f;
    --card-grey-light: #777777;
    --ink-red: #8e1518;
    --portrait-top: #7c7c7c;
    --portrait-mid: #4a4a4a;
    --portrait-dark: #1e1e1e;
  }
  * { margin: 0; padding: 0; box-sizing: border-box; }
  html, body {
    width: 1200px;
    height: 720px;
    overflow: hidden;
    background: var(--card-grey);
  }
  .card {
    position: relative;
    width: 1200px;
    height: 720px;
    background: linear-gradient(160deg, var(--card-grey-light) 0%, var(--card-grey) 55%, #666 100%);
    font-family: "Urbanist", "Century Gothic", sans-serif;
    color: var(--ink-red);
    overflow: hidden;
  }
  .identity {
    position: absolute;
    left: 90px;
    top: 228px;
    width: 560px;
  }
  .identity__name {
    font-size: 62px;
    font-weight: 700;
    letter-spacing: 0.5px;
    line-height: 1;
  }
  .identity__role {
    margin-top: 8px;
    margin-left: 44px;
    font-size: 27px;
    font-weight: 400;
    letter-spacing: 8px;
  }
  .contacts {
    position: absolute;
    left: 90px;
    top: 372px;
    width: 560px;
    font-size: 24px;
    line-height: 1.45;
  }
  .contacts__line { text-align: center; }
  .contacts__line--email { text-align: left; }
  .contacts__label { font-weight: 700; }
  .contacts__web {
    margin-top: 36px;
    margin-left: 30px;
    font-size: 26px;
  }
  .contacts__web strong { font-weight: 700; }
  .portrait {
    position: absolute;
    right: 0;
    top: 0;
    width: 470px;
    height: 640px;
    background: linear-gradient(170deg, var(--portrait-top) 0%, var(--portrait-mid) 55%, var(--portrait-dark) 100%);
  }
</style>
</head>
<body>
  <main class="card">
    <section class="identity">
      <h1 class="identity__name">Paul Ostrander</h1>
      <p class="identity__role">Crime Novelist</p>
    </section>
    <section class="contacts">
      <p class="contacts__line"><span class="contacts__label">Ph:</span> 0064 27 5139427</p>
      <p class="contacts__line contacts__line--email"><span class="contacts__label">Email:</span> paulbostrander@mailbox.example</p>
      <p class="contacts__web">www.<strong>ostranderthrillers</strong>.example</p>
    </section>
    <div class="portrait" role="img" aria-label="Portrait photograph of the author"></div>
  </main>
</body>
</html>
```